Junk Removal Website Design

We are working with a Junk Removal company in California. They provide junk hauling services for commercial and residential throughout California.
Some sites to use for inspiration:
https://www.clearbarrowhauls.com
https://pebblecartworkteam.com
https://www.fernwayliftersandmovers.com
https://www.mistoakcleanupcrew.com
Thank you for taking the time to consider designing a website for us. We are web developers based in Stockton, CA, USA. Most of our projects go through the same process. Understanding this process may help you win a project with us. We custom-code all of our websites in-house. We don’t have any requirements as to what tools you use for your design, but we ask that you follow these guidelines.
IMAGES:
If you use any images or icons in the design, we ask that you have a link to the asset so we can purchase the image/icon. Most of the designs we submit do not have the customer’s images on them unless they have some great images. Be creative; show us the feeling you are trying to portray with your image choices. Use any royalty-free site you choose. We subscribe to Vontrel and mainly use their images, but we can purchase images outside of Vontrel. PLEASE NOTE: we will not submit designs to clients with watermarks on the images.
FONTS:
We ask that you identify the fonts you’re using in the design. This can be done in a message if you want. We typically use Quimbly Fonts and Vontrel Fonts.
CONTENT:
We're always open to different content and ideas. We often submit designs with stock images so the client can see our vision. We typically take pictures after the website launch to use their images with our vision. Lorem Ipsum is fine for paragraphs, but we ask that you make the Headers with correct English. We want to be able to show the vision and identify the sections of the website.
INSPIRATION:
We typically add a couple of links in the brief of websites we like to help you get started in your design.
REVISIONS:
We do not often ask for revisions of the designs unless we see something in the design that may not appeal to the client. If there are slight changes that we want to make, we do that in the development process.
FEEDBACK:
We rarely give feedback on designs during the design process. We are working on many website projects and do not have the time to provide feedback. We usually respond if your request is well thought out and asks specific questions, but a note asking “feedback, please” usually goes unanswered.
Number of Pages Required
1 page

```html
<!DOCTYPE html>
<html lang="en">
<head>
<meta charset="utf-8">
<title>Clutterwell Hauling</title>
<link href="https://fonts.googleapis.com/css2?family=Outfit:wght@400;500;600;700;800&family=Poppins:wght@400;500;600&display=swap" rel="stylesheet">
<style>
:root{
  --green:#4aa544;
  --green-dark:#3b8f36;
  --green-light:#deeed8;
  --ink:#1c1d22;
  --text:#3a3a3a;
  --muted:#8a8a8a;
  --white:#fff;
  --field:#eeeeee;
  --placeholder:#e6e8e4;
}
*{margin:0;padding:0;box-sizing:border-box}
html,body{width:1200px;height:4874px;overflow:hidden}
body{position:relative;background:var(--white);font-family:'Poppins',sans-serif;color:var(--text)}
.abs{position:absolute}
.head{font-family:'Outfit',sans-serif;font-weight:800;color:var(--ink);text-transform:uppercase;letter-spacing:-1px;line-height:1.08}
.sub{font-family:'Outfit',sans-serif;font-weight:700;font-size:14px;color:var(--ink);text-transform:uppercase}
.rule{height:3px;background:var(--green)}
.btn{display:flex;align-items:center;justify-content:center;gap:10px;font-family:'Outfit',sans-serif;font-weight:700;font-size:9px;letter-spacing:2px;color:#fff;text-transform:uppercase;border-radius:3px}
.btn svg{width:22px;height:8px}
.btn-dark{background:var(--ink)}
.btn-green{background:var(--green)}
.photo{border-radius:10px}

/* header */
.brand{left:199px;top:22px;width:190px;font-family:'Outfit',sans-serif;font-weight:800;font-size:30px;line-height:0.95;color:var(--green)}
.contact-item{display:flex;align-items:center;gap:14px;font-size:12px;color:var(--ink)}
.contact-item .dot{width:30px;height:30px;border-radius:50%;background:var(--ink);display:flex;align-items:center;justify-content:center}
.search{left:933px;top:17px;width:203px;height:27px;background:var(--field);border-radius:4px;font-size:7px;color:#777;padding:9px 16px;letter-spacing:.5px}
.nav{left:424px;top:59px;width:776px;height:75px;background:var(--green);clip-path:polygon(20px 0,100% 0,100% 100%,0 100%,8px 10px);border-bottom-left-radius:8px}
.nav ul{list-style:none;position:absolute;left:60px;top:31px;display:flex;gap:32px;font-size:11px;color:#fff}
.nav .btn{position:absolute;left:577px;top:22px;width:135px;height:31px}

/* hero */
.hero-photo{left:0;top:117px;width:1200px;height:653px;background:linear-gradient(110deg,#3f6a2f 0%,#7fa070 30%,#c9d3c6 55%,#e8ecea 75%,#b54a4a 100%)}
.hero-title{left:615px;top:232px;font-size:54px}
.hero-sub{left:615px;top:362px}
.card{left:197px;top:680px;width:804px;height:170px;background:#fff;border-radius:12px;box-shadow:0 10px 30px rgba(0,0,0,.12)}
.field{left:591px;top:729px;width:342px;height:36px;background:var(--field);border-radius:5px;font-size:9px;color:#888;padding:12px 28px}

/* services */
.services-bg{left:0;top:1478px;width:1200px;height:894px;background:var(--green-light)}
.svc{top:1689px;width:322px;height:386px;border-radius:10px;overflow:hidden}
.svc .img{width:100%;height:100%}
.svc span{position:absolute;left:0;right:0;bottom:26px;text-align:center;font-family:'Outfit',sans-serif;font-weight:800;font-size:14px;color:#fff;text-transform:uppercase}
.arrow-btn{width:34px;height:34px;border-radius:50%;background:var(--green);display:flex;align-items:center;justify-content:center}
.band{left:0;top:2164px;width:962px;height:208px;background:var(--green);clip-path:polygon(0 0,928px 0,962px 180px,950px 208px,0 208px);border-top-right-radius:20px}
.band-item{width:200px;text-align:center;font-family:'Outfit',sans-serif;font-weight:700;font-size:13px;color:#fff;text-transform:uppercase;line-height:1.35}
.band-divider{top:2210px;width:2px;height:110px;background:rgba(255,255,255,.7)}

/* steps */
.step-label{font-family:'Outfit',sans-serif;font-weight:800;font-size:14px;color:var(--ink);text-transform:uppercase;text-align:center;width:255px}

/* reviews */
.review{left:197px;top:3269px;width:380px;height:157px;background:#fff;border-radius:10px;box-shadow:0 8px 28px rgba(0,0,0,.1)}

/* rescue */
.badge{width:188px;height:100px;background:#fff;border-radius:8px;box-shadow:0 6px 22px rgba(0,0,0,.09);display:flex;align-items:center;justify-content:center}
.badge-mark{background:var(--placeholder)}

/* footer */
.footer{left:0;top:4360px;width:1200px;height:514px;background:var(--ink)}
.cta{left:227px;top:4261px;width:973px;height:210px;background:var(--green);clip-path:polygon(40px 0,100% 0,100% 100%,0 100%);border-top-left-radius:14px}
.foot-title{font-family:'Outfit',sans-serif;font-weight:600;font-size:14px;color:#fff}
.foot-text{font-size:11px;color:#e6e6e6}
.foot-icon{width:30px;height:30px;border-radius:50%;border:1px solid #3d3e44;display:flex;align-items:center;justify-content:center}
.social{width:27px;height:27px;border-radius:50%;background:var(--green)}
.vline{width:1px;background:#44454b}
</style>
</head>
<body>

<!-- HEADER -->
<div class="abs brand">CLUTTERWELL<br>HAULING</div>
<div class="abs contact-item" style="left:496px;top:15px">
  <span class="dot"><svg width="12" height="12" viewBox="0 0 24 24"><path fill="#fff" d="M6.6 10.8a15 15 0 006.6 6.6l2.2-2.2c.3-.3.7-.4 1-.2 1.1.4 2.3.6 3.6.6.6 0 1 .4 1 1V20c0 .6-.4 1-1 1A17 17 0 013 4c0-.6.4-1 1-1h3.5c.6 0 1 .4 1 1 0 1.3.2 2.5.6 3.6.1.3 0 .7-.2 1z"/></svg></span>833-555-0148
</div>
<div class="abs contact-item" style="left:702px;top:15px">
  <span class="dot"><svg width="12" height="10" viewBox="0 0 24 18"><rect x="1" y="1" width="22" height="16" rx="2" fill="var(--green)"/><path d="M2 2l10 8 10-8" stroke="#fff" stroke-width="2" fill="none"/></svg></span>hello@clutterwellhauling.com
</div>
<div class="abs search">SEARCH...
  <svg class="abs" style="right:12px;top:8px" width="11" height="11" viewBox="0 0 24 24"><circle cx="10" cy="10" r="7" stroke="#999" stroke-width="2.5" fill="none"/><path d="M15 15l6 6" stroke="#999" stroke-width="2.5"/></svg>
</div>
<nav class="abs nav">
  <ul><li>Who We Are</li><li>What We Remove</li><li>Jobs We Do</li><li>Our Work</li><li>Blog</li><li>Faq</li></ul>
  <div class="btn btn-dark">Contact Us <svg viewBox="0 0 22 8"><path d="M0 4h20M17 1l3 3-3 3" stroke="#fff" fill="none"/></svg></div>
</nav>

<!-- HERO -->
<div class="abs hero-photo" role="img" aria-label="Crew in hi-vis vests loading a yellow bin into a green garbage truck beside colourful wheelie bins"></div>
<h1 class="abs head hero-title">We Make<br>Junk Disappear.</h1>
<p class="abs sub hero-sub">All you have to do is point!</p>
<div class="abs rule" style="left:615px;top:387px;width:159px"></div>

<div class="abs card"></div>
<h2 class="abs head" style="left:265px;top:731px;font-size:27px;letter-spacing:-.5px">Tell our team what<br>you want gone!</h2>
<div class="abs rule" style="left:265px;top:805px;width:158px"></div>
<div class="abs field">ENTER YOUR ZIP CODE</div>
<div class="abs btn btn-green" style="left:591px;top:778px;width:164px;height:30px">Check Availability <svg viewBox="0 0 22 8"><path d="M0 4h20M17 1l3 3-3 3" stroke="#fff" fill="none"/></svg></div>

<!-- ABOUT -->
<h2 class="abs head" style="left:197px;top:962px;font-size:48px">Cleaning what<br>you want</h2>
<p class="abs sub" style="left:197px;top:1083px">All you have to do is point!</p>
<p class="abs" style="left:197px;top:1130px;width:432px;font-size:11.5px;line-height:21px">Lorem Ipsum is simply dummy text of the printing and typesetting industry. Lorem Ipsum has been the industry's standard dummy text ever since the 1500s, when an unknown printer took a galley of type and scrambled it to make a type specimen book. It has survived not only five centuries, but also the leap into electronic typesetting, remaining essentially unchanged.</p>
<p class="abs" style="left:197px;top:1259px;width:440px;font-size:11.5px;line-height:21px">It was popularised in the 1960s with the release of Lettrelle sheets containing Lorem Ipsum passages, and more recently with desktop publishing software like Pressmark Layout including versions of Lorem Ipsum.</p>
<div class="abs btn btn-dark" style="left:197px;top:1348px;width:134px;height:30px">Learn More <svg viewBox="0 0 22 8"><path d="M0 4h20M17 1l3 3-3 3" stroke="#fff" fill="none"/></svg></div>
<div class="abs" role="img" aria-label="Worker in a yellow hard hat wheeling a yellow bin toward a green garbage truck" style="left:685px;top:933px;width:515px;height:464px;background:linear-gradient(135deg,#5f9a3a,#a5c07a 45%,#3b6ea8 70%,#d8b92a);clip-path:polygon(60px 0,100% 0,100% 100%,0 100%);border-top-left-radius:24px;border-bottom-left-radius:24px"></div>

<!-- SERVICES -->
<div class="abs services-bg"></div>
<h2 class="abs head" style="left:0;width:1200px;text-align:center;top:1576px;font-size:45px">Our Removal Services</h2>
<p class="abs sub" style="left:0;width:1200px;text-align:center;top:1636px">Suffice it to say, dang near anything!</p>
<div class="abs rule" style="left:520px;top:1659px;width:160px"></div>
<div class="abs svc" style="left:93px"><div class="img" role="img" aria-label="Pile of cardboard boxes and household clutter" style="background:linear-gradient(180deg,#c9c5bb,#9e8060 55%,#1a1a1a)"></div><span>Residential</span></div>
<div class="abs svc" style="left:439px"><div class="img" role="img" aria-label="Old sofa and furniture left at a curb" style="background:linear-gradient(180deg,#5f7a4a,#6d5a45 55%,#151515)"></div><span>Furniture Removal</span></div>
<div class="abs svc" style="left:784px"><div class="img" role="img" aria-label="Discarded appliances piled on a suburban lawn" style="background:linear-gradient(180deg,#8fae73,#b5a792 55%,#161616)"></div><span>Appliance Removal</span></div>
<div class="abs arrow-btn" style="left:66px;top:1859px"><svg width="10" height="10" viewBox="0 0 10 10"><path d="M7 1L3 5l4 4" stroke="#fff" stroke-width="1.6" fill="none"/></svg></div>
<div class="abs arrow-btn" style="left:1100px;top:1859px"><svg width="10" height="10" viewBox="0 0 10 10"><path d="M3 1l4 4-4 4" stroke="#fff" stroke-width="1.6" fill="none"/></svg></div>

<div class="abs band"></div>
<svg class="abs" style="left:164px;top:2228px" width="40" height="50" viewBox="0 0 40 50"><path d="M20 2C10 2 3 9 3 19c0 12 17 29 17 29s17-17 17-29C37 9 30 2 20 2z" fill="#fff"/><circle cx="20" cy="19" r="7" fill="var(--green)"/></svg>
<div class="abs band-item" style="left:84px;top:2302px">Find a Location</div>
<div class="abs band-divider" style="left:305px"></div>
<svg class="abs" style="left:428px;top:2218px" width="48" height="48" viewBox="0 0 48 48"><rect x="10" y="14" width="28" height="20" rx="4" transform="rotate(-45 24 24)" fill="#fff"/><circle cx="32" cy="13" r="3" fill="var(--green)"/><path d="M20 22h8M20 27h6" stroke="var(--green)" stroke-width="2.5"/></svg>
<div class="abs band-item" style="left:352px;top:2290px">Learn more about<br>our pricing</div>
<div class="abs band-divider" style="left:598px"></div>
<svg class="abs" style="left:707px;top:2218px" width="44" height="50" viewBox="0 0 44 50"><path d="M6 4h26l6 6v36H6z" fill="#fff"/><path d="M12 16h20M12 23h20M12 30h14" stroke="var(--green)" stroke-width="2.5"/><path d="M14 40l4 4 8-8" stroke="var(--green)" stroke-width="2.5" fill="none"/></svg>
<div class="abs band-item" style="left:629px;top:2290px">Get a free quote<br>online</div>

<!-- STEPS -->
<h2 class="abs head" style="left:0;width:1200px;text-align:center;top:2457px;font-size:45px">Expert staff + heavy<br>duty trucks</h2>
<p class="abs sub" style="left:0;width:1200px;text-align:center;top:2573px">The winning formula</p>
<div class="abs rule" style="left:520px;top:2598px;width:160px"></div>
<div class="abs photo" role="img" aria-label="Crew loading a green bin into a truck" style="left:197px;top:2592px;width:255px;height:219px;background:linear-gradient(160deg,#6a6a5e,#8db24f 60%,#4b6f3a)"></div>
<div class="abs photo" role="img" aria-label="Worker beside a garbage truck on a residential street" style="left:471px;top:2631px;width:256px;height:222px;background:linear-gradient(160deg,#9fb7c9,#7f858a 55%,#59615a)"></div>
<div class="abs photo" role="img" aria-label="Dump truck tipping a load of junk at a landfill" style="left:746px;top:2592px;width:255px;height:219px;background:linear-gradient(180deg,#3b88d6,#8fbce6 45%,#8a6d46 70%,#5a4a38)"></div>
<div class="abs step-label" style="left:197px;top:2830px">Load it</div>
<div class="abs step-label" style="left:471px;top:2871px">Haul it</div>
<div class="abs step-label" style="left:746px;top:2830px">Dump it!</div>
<div class="abs btn btn-green" style="left:523px;top:2911px;width:151px;height:29px">Call Us Today <svg viewBox="0 0 22 8"><path d="M0 4h20M17 1l3 3-3 3" stroke="#fff" fill="none"/></svg></div>

<!-- REVIEWS -->
<div class="abs" style="left:615px;top:3023px;width:585px;height:523px;background:var(--green-light);clip-path:polygon(105px 0,100% 0,100% 100%,0 100%);border-bottom-left-radius:18px"></div>
<div class="abs" role="img" aria-label="Smiling young man in a white t-shirt with arms crossed" style="left:748px;top:2959px;width:312px;height:587px;background:linear-gradient(180deg,#d7cbbd 0%,#ece9e4 40%,#f4f4f2 100%);border-radius:140px 140px 0 0"></div>
<h2 class="abs head" style="left:197px;top:3083px;font-size:45px">We love our<br>valued customers!</h2>
<p class="abs sub" style="left:197px;top:3200px">Here's what they are saying:</p>
<div class="abs review"></div>
<p class="abs" style="left:246px;top:3296px;width:300px;font-size:10.5px;line-height:21px">Explained very well the cost and did exactly what they said they would. Staff were very friendly and accommodating. Very professional and courteous. I would highly recommend their services. "</p>
<p class="abs" style="left:246px;top:3389px;font-family:'Outfit',sans-serif;font-weight:700;font-size:8.5px;color:var(--green)">DANA WHITLOW - REVIEW</p>
<p class="abs" style="left:418px;top:3386px;font-size:10px;color:var(--ink);letter-spacing:1px">★★★★★</p>
<div class="abs" style="left:229px;top:3454px;width:25px;height:25px;border-radius:50%;background:var(--green)"></div>
<svg class="abs" style="left:236px;top:3461px" width="40" height="11" viewBox="0 0 40 11"><path d="M5 1L1 5.5 5 10M1 5.5h38" stroke="var(--ink)" stroke-width="1.5" fill="none"/></svg>
<div class="abs" style="left:310px;top:3450px;width:33px;height:33px;border-radius:50%;background:var(--green)"></div>
<svg class="abs" style="left:290px;top:3461px" width="46" height="11" viewBox="0 0 46 11"><path d="M0 5.5h44M40 1l4 4.5-4 4.5" stroke="var(--ink)" stroke-width="1.5" fill="none"/></svg>

<!-- RESCUE -->
<div class="abs" role="img" aria-label="Worker in a hard hat standing by a green garbage truck with bins and bags" style="left:0;top:3629px;width:570px;height:526px;background:linear-gradient(120deg,#7aa35c,#5fbf3a 50%,#3d6a2b 80%,#2a2a2a);clip-path:polygon(0 0,480px 0,570px 460px,540px 526px,0 526px);border-bottom-right-radius:24px"></div>
<h2 class="abs head" style="left:609px;top:3688px;font-size:45px">Need a junk<br>rescue?</h2>
<p class="abs sub" style="left:609px;top:3785px">Reach out to us today!</p>
<div class="abs badge" style="left:609px;top:3845px"><div class="badge-mark" role="img" aria-label="Review rating badge" style="width:110px;height:44px;border-radius:6px"></div></div>
<div class="abs badge" style="left:814px;top:3845px"><div class="badge-mark" role="img" aria-label="Award badge" style="width:64px;height:64px;border-radius:50%"></div></div>
<div class="abs badge" style="left:609px;top:3968px"><div class="badge-mark" role="img" aria-label="Local listing badge" style="width:72px;height:56px;border-radius:6px"></div></div>
<div class="abs badge" style="left:814px;top:3968px"><div class="badge-mark" role="img" aria-label="Eco-friendly disposal badge" style="width:60px;height:60px;border-radius:6px"></div></div>

<!-- CTA + FOOTER -->
<div class="abs footer"></div>
<div class="abs cta"></div>
<h2 class="abs head" style="left:356px;top:4322px;font-size:42px;color:#fff">Fast, friendly &amp;<br>affordable</h2>
<p class="abs" style="left:795px;top:4338px;width:160px;font-size:10px;line-height:18px;color:#fff">Choose us for a complete haul-away service!</p>
<div class="abs btn" style="left:795px;top:4388px;width:144px;height:30px;background:#fff;color:var(--ink)">Get In Touch <svg viewBox="0 0 22 8"><path d="M0 4h20M17 1l3 3-3 3" stroke="var(--ink)" fill="none"/></svg></div>

<div class="abs brand" style="left:199px;top:4562px;color:var(--green);font-size:27px">CLUTTERWELL<br>HAULING</div>
<div class="abs foot-icon" style="left:201px;top:4676px"><svg width="11" height="11" viewBox="0 0 24 24"><path fill="var(--green)" d="M6.6 10.8a15 15 0 006.6 6.6l2.2-2.2c.3-.3.7-.4 1-.2 1.1.4 2.3.6 3.6.6.6 0 1 .4 1 1V20c0 .6-.4 1-1 1A17 17 0 013 4c0-.6.4-1 1-1h3.5c.6 0 1 .4 1 1 0 1.3.2 2.5.6 3.6.1.3 0 .7-.2 1z"/></svg></div>
<div class="abs foot-icon" style="left:259px;top:4676px"><svg width="12" height="9" viewBox="0 0 24 18"><rect x="1" y="1" width="22" height="16" rx="2" fill="var(--green)"/><path d="M2 2l10 8 10-8" stroke="var(--ink)" stroke-width="2" fill="none"/></svg></div>
<div class="abs foot-icon" style="left:316px;top:4676px"><svg width="10" height="12" viewBox="0 0 40 50"><path d="M20 2C10 2 3 9 3 19c0 12 17 29 17 29s17-17 17-29C37 9 30 2 20 2z" fill="var(--green)"/></svg></div>

<div class="abs vline" style="left:432px;top:4553px;height:227px"></div>
<p class="abs foot-title" style="left:515px;top:4558px">Working Hours</p>
<p class="abs foot-text" style="left:515px;top:4600px">Mon - Fri7:00 am - 7:00 pm</p>
<p class="abs foot-text" style="left:515px;top:4626px">Saturday7:30 am - 6:30 pm</p>
<p class="abs foot-text" style="left:515px;top:4653px">Sunday9:00 am - 5:00 pm</p>
<p class="abs foot-text" style="left:515px;top:4687px">Sunday: no pick-ups, only phone calls</p>
<div class="abs social" style="left:513px;top:4721px"></div>
<div class="abs social" style="left:559px;top:4721px"></div>
<div class="abs social" style="left:606px;top:4721px"></div>

<div class="abs vline" style="left:803px;top:4553px;height:227px"></div>
<p class="abs foot-title" style="left:884px;top:4558px">Links</p>
<p class="abs foot-text" style="left:884px;top:4597px">Who We Are</p>
<p class="abs foot-text" style="left:884px;top:4623px">What We Remove</p>
<p class="abs foot-text" style="left:884px;top:4650px">Jobs We Do</p>
<p class="abs foot-text" style="left:884px;top:4676px">Our Work</p>
<p class="abs foot-text" style="left:884px;top:4702px">Blog</p>
<p class="abs foot-text" style="left:884px;top:4728px">Faq</p>

<div class="abs" style="left:0;top:4837px;width:1200px;height:1px;background:#3a3b41"></div>
<p class="abs foot-text" style="left:0;width:1200px;text-align:center;top:4849px;font-size:10px">© 2023 All Rights Reserved | Brightlane Listings LLC D.B.A. Clutterwell Hauling</p>

</body>
</html>
```